Letterhead and Stationary for Construction Company

Brisk Current needs modern Letterhead, Envelopes and Notepad designs.

Industry/Entity Type

Construction

Colors
f78f20
34a7d8
ffffff

Requirements
Must have
• Modern looking design.

```html
<!DOCTYPE html>
<html lang="en">
<head>
<meta charset="utf-8">
<title>Brisk Current Letterhead</title>
<link href="https://fonts.googleapis.com/css2?family=Open+Sans:wght@400;700&display=swap" rel="stylesheet">
<style>
  :root {
    --orange: #f78f20;
    --orange-deep: #e0661f;
    --blue: #1f5fa8;
    --ink: #1d2a3a;
    --paper: #ffffff;
    --backdrop: #dcbc8c;
  }
  * { margin: 0; padding: 0; box-sizing: border-box; }
  html, body { width: 1200px; height: 784px; overflow: hidden; }
  body {
    background: var(--backdrop);
    font-family: "Open Sans", Arial, sans-serif;
  }
  .letterhead {
    position: absolute;
    left: 330px;
    top: 12px;
    width: 540px;
    height: 760px;
    background: var(--paper);
    overflow: hidden;
    box-shadow: 0 6px 18px rgba(90, 60, 20, 0.25);
  }
  .header-art { position: absolute; left: 0; top: 0; width: 540px; height: 130px; }
  .brand {
    position: absolute;
    left: 20px;
    top: 28px;
    display: flex;
    align-items: center;
    gap: 7px;
    white-space: nowrap;
  }
  .brand-mark {
    width: 18px; height: 18px;
    border-radius: 50%;
    background: var(--orange);
    flex: none;
  }
  .brand-name {
    font-weight: 700;
    font-size: 19px;
    line-height: 1;
    color: var(--orange-deep);
    letter-spacing: -0.3px;
  }
  .address {
    position: absolute;
    left: 244px;
    top: 100px;
    font-size: 9px;
    font-weight: 700;
    color: var(--ink);
    white-space: nowrap;
  }
  .contact {
    position: absolute;
    right: 20px;
    top: 22px;
    font-size: 8px;
    line-height: 15px;
    color: var(--paper);
    text-align: right;
  }
  .contact-row { display: flex; gap: 14px; justify-content: flex-end; }
  .contact-item { display: flex; align-items: center; gap: 4px; white-space: nowrap; }
  .contact-item svg { width: 8px; height: 8px; }
  .bottom-edge {
    position: absolute;
    left: 0; bottom: 0;
    width: 100%; height: 7px;
    background: var(--orange-deep);
  }
</style>
</head>
<body>
  <main class="letterhead">
    <svg class="header-art" viewBox="0 0 540 130" aria-hidden="true">
      <defs>
        <linearGradient id="band-fill" x1="0" y1="0" x2="1" y2="0">
          <stop offset="0" stop-color="#e0661f"/>
          <stop offset="1" stop-color="#f78f20"/>
        </linearGradient>
      </defs>
      <rect x="0" y="0" width="18" height="7" fill="#e0661f"/>
      <rect x="18" y="0" width="204" height="7" fill="#1f5fa8"/>
      <polygon points="222,0 540,0 540,88 236,88 215,68 215,7 222,7" fill="url(#band-fill)"/>
      <polygon points="215,60 243,80 540,80 540,88 236,88 215,68" fill="#1f5fa8"/>
      <polygon points="215,60 215,52 223,58" fill="#1f5fa8"/>
    </svg>

    <div class="brand">
      <span class="brand-mark"></span>
      <span class="brand-name">Brisk Current</span>
    </div>

    <p class="address">12 Harbour Row Millbrook Vale MB04 7TQ</p>

    <div class="contact">
      <div class="contact-row">
        <span class="contact-item">
          <svg viewBox="0 0 10 10"><path d="M2 1l2 2-1 1.5c.8 1.4 1.6 2.2 3 3L7.5 6l2 2-1.5 1.5C4.5 9 1 5.5.5 2z" fill="#fff"/></svg>
          (01632) 960481
        </span>
        <span class="contact-item">
          <svg viewBox="0 0 10 10"><path d="M2 1l2 2-1 1.5c.8 1.4 1.6 2.2 3 3L7.5 6l2 2-1.5 1.5C4.5 9 1 5.5.5 2z" fill="#fff"/></svg>
          (01632) 960482
        </span>
      </div>
      <div class="contact-row">
        <span class="contact-item">
          <svg viewBox="0 0 10 10"><rect x=".5" y="2" width="9" height="6" fill="none" stroke="#fff"/><path d="M.5 2L5 5.5 9.5 2" fill="none" stroke="#fff"/></svg>
          hello@briskcurrent.com
        </span>
        <span class="contact-item">
          <svg viewBox="0 0 10 10"><circle cx="5" cy="5" r="4.2" fill="none" stroke="#fff"/><path d="M.8 5h8.4M5 .8c-2.4 2.6-2.4 5.8 0 8.4M5 .8c2.4 2.6 2.4 5.8 0 8.4" fill="none" stroke="#fff" stroke-width=".7"/></svg>
          www.briskcurrent.com
        </span>
      </div>
    </div>

    <div class="bottom-edge"></div>
  </main>
</body>
</html>
```